Brell Harbor Company Business Cards

Front and Back Business Card - logo and text setup - cool design. I need workable photoshop or illustrator files so I can setup each employee card with design that is created
Updates

Hi everyone, thank you for the great entries. Please no more white and blue cards - there are so many already - black and silver only now please. thanks!

Target Market(s)

Construction Industry - Facility Managers

Industry/Entity Type

Construction

Contact Information for Business Card

I really like contemporary simplistic looks - clean neat....not opposed to seeing some black backrounds

Requirements
Must have
• Logo/website address with design on front only - www.brellharbor-example.com (logo attached)
• Back:
• Name/Title/Company Address/Phone/email address
Nice to have
• Cool design
Should not have
• Nothing gimmicky like Fire or Water - since we are a Fire Protection company - it has all been done

```html
<!DOCTYPE html>
<html lang="en">
<head>
<meta charset="utf-8">
<title>Brell Harbor Company – Business Cards</title>
<link href="https://fonts.googleapis.com/css2?family=Lato:wght@400;700;900&display=swap" rel="stylesheet">
<style>
  :root {
    --page: #ffffff;
    --card-dark: #0f1213;
    --card-mid: #1c1f21;
    --card-light: #2f3436;
    --accent: #ff2a1d;
    --rule: #0b0d0e;
  }
  html, body {
    margin: 0;
    padding: 0;
    width: 1200px;
    height: 1200px;
    overflow: hidden;
    background: var(--page);
    font-family: "Lato", sans-serif;
  }
  .sheet {
    position: relative;
    width: 1200px;
    height: 1200px;
  }
  .card {
    position: absolute;
    left: 140px;
    width: 900px;
    height: 540px;
    overflow: hidden;
    background:
      repeating-linear-gradient(135deg, rgba(255,255,255,0.018) 0 1px, transparent 1px 4px),
      linear-gradient(100deg, var(--card-light) 0%, var(--card-mid) 30%, var(--card-dark) 70%, #131617 100%);
  }
  .card--front { top: 50px; }
  .card--back { top: 618px; }

  .front-arc {
    position: absolute;
    inset: 0;
    width: 900px;
    height: 540px;
  }

  .contact {
    position: absolute;
    left: 76px;
    top: 0;
    color: var(--accent);
  }
  .contact__name {
    position: absolute;
    top: 72px;
    left: 0;
    margin: 0;
    font-size: 38px;
    font-weight: 700;
    white-space: nowrap;
    letter-spacing: 0.2px;
  }
  .contact__title {
    position: absolute;
    top: 116px;
    left: 0;
    margin: 0;
    font-size: 24px;
    font-weight: 400;
    white-space: nowrap;
  }
  .contact__rule {
    position: absolute;
    left: 0;
    height: 4px;
    background: linear-gradient(90deg, var(--rule) 0%, rgba(11,13,14,0.7) 70%, rgba(40,44,46,0.6) 100%);
  }
  .contact__rule--one { top: 148px; width: 360px; }
  .contact__rule--two { top: 258px; width: 380px; }
  .contact__address {
    position: absolute;
    top: 200px;
    left: 0;
    margin: 0;
    font-size: 22px;
    line-height: 27px;
    font-weight: 400;
    font-style: normal;
    white-space: nowrap;
  }
  .contact__line {
    position: absolute;
    left: -6px;
    display: flex;
    align-items: center;
    gap: 10px;
    font-size: 22px;
    white-space: nowrap;
  }
  .contact__line--phone { top: 324px; }
  .contact__line--mail { top: 365px; }
  .contact__icon {
    width: 24px;
    height: 24px;
    fill: var(--accent);
    flex: none;
  }

  .wordmark {
    position: absolute;
    display: flex;
    align-items: center;
    gap: 12px;
    color: var(--accent);
    font-weight: 900;
    white-space: nowrap;
  }
  .wordmark__square {
    background: var(--accent);
    flex: none;
  }
  .wordmark--front {
    left: 524px;
    top: 240px;
    font-size: 44px;
  }
  .wordmark--front .wordmark__square { width: 22px; height: 22px; }
  .wordmark--back {
    left: 0;
    right: 0;
    top: 212px;
    justify-content: center;
    font-size: 64px;
  }
  .wordmark--back .wordmark__square { width: 30px; height: 30px; }

  .website {
    position: absolute;
    left: 0;
    right: 0;
    top: 336px;
    text-align: center;
    color: var(--accent);
    font-size: 22px;
    font-weight: 700;
    letter-spacing: 6px;
    white-space: nowrap;
  }
</style>
</head>
<body>
<main class="sheet">

  <section class="card card--front" aria-label="Card front">
    <svg class="front-arc" viewBox="0 0 900 540" aria-hidden="true">
      <defs>
        <linearGradient id="arcShade" x1="0" y1="0" x2="1" y2="0">
          <stop offset="0" stop-color="#0a0c0d" stop-opacity="0.9"/>
          <stop offset="1" stop-color="#0a0c0d" stop-opacity="0"/>
        </linearGradient>
      </defs>
      <path d="M328 0 Q 520 140 500 300 Q 480 440 290 540 L 340 540 Q 500 440 520 300 Q 540 140 360 0 Z" fill="url(#arcShade)"/>
      <path d="M355 0 Q 540 140 516 300 Q 495 430 330 540" fill="none" stroke="#24282a" stroke-width="3" opacity="0.7"/>
    </svg>

    <div class="contact">
      <h1 class="contact__name">Daniel Reyes</h1>
      <p class="contact__title">Founder</p>
      <div class="contact__rule contact__rule--one"></div>
      <address class="contact__address">48 Linden Avenue<br>Tampa, FL 33602</address>
      <div class="contact__rule contact__rule--two"></div>
      <div class="contact__line contact__line--phone">
        <svg class="contact__icon" viewBox="0 0 24 24" aria-hidden="true"><path d="M6.6 10.8a15.2 15.2 0 0 0 6.6 6.6l2.2-2.2c.3-.3.7-.4 1-.2 1.1.4 2.3.6 3.6.6.6 0 1 .4 1 1V20c0 .6-.4 1-1 1A17 17 0 0 1 3 4c0-.6.4-1 1-1h3.5c.6 0 1 .4 1 1 0 1.3.2 2.5.6 3.6.1.3 0 .7-.2 1z"/></svg>
        <span>000-000-000</span>
      </div>
      <div class="contact__line contact__line--mail">
        <svg class="contact__icon" viewBox="0 0 24 24" aria-hidden="true"><path d="M2 5h20v2l-10 6L2 7z"/><path d="M2 9l10 6 10-6v10H2z"/></svg>
        <span>info@brellharbor-example.com</span>
      </div>
    </div>

    <div class="wordmark wordmark--front">
      <span class="wordmark__square"></span>
      <span class="wordmark__name">Brell Harbor</span>
    </div>
  </section>

  <section class="card card--back" aria-label="Card back">
    <div class="wordmark wordmark--back">
      <span class="wordmark__square"></span>
      <span class="wordmark__name">Brell Harbor</span>
    </div>
    <p class="website">www.brellharbor-example.com</p>
  </section>

</main>
</body>
</html>
```